Korvane Works Business cards

We require somebody to design business cards for our new business.

Target Market(s)

Mining, haulage and civil.

Industry/Entity Type

Auto electrician in mining industry

Contact Information for Business Card

ABN, business email address, mobile number.

Colors
00AB8E
00BBA5
67D7C9
C6EFE9
E9F9F6

Requirements
Must have
• Services I offer: Breakdowns, Field Service, A/C Systems, Machine rewires, mine site vehicle fit outs

```html
<!DOCTYPE html>
<html lang="en">
<head>
<meta charset="UTF-8">
<title>Korvane Works Business Cards</title>
<link href="https://fonts.googleapis.com/css2?family=Exo+2:ital,wght@0,400;0,600;0,800;1,800&display=swap" rel="stylesheet">
<style>
  :root {
    --teal-deep: #00AB8E;
    --teal: #00BBA5;
    --teal-light: #67D7C9;
    --teal-pale: #C6EFE9;
    --teal-mist: #E9F9F6;
    --card-black: #0b0c0d;
    --card-gloss: #1c1e20;
    --silver: #b9bdc0;
    --ink: #e8ecec;
    --backdrop: #d9d6d0;
  }
  * { box-sizing: border-box; margin: 0; padding: 0; }
  html, body { width: 1200px; height: 917px; overflow: hidden; }
  body {
    background: var(--backdrop);
    font-family: "Exo 2", sans-serif;
    position: relative;
  }
  .card {
    position: absolute;
    background: linear-gradient(150deg, var(--card-gloss) 0%, var(--card-black) 55%, #050606 100%);
    box-shadow: 0 14px 30px rgba(0,0,0,.35);
    color: var(--ink);
    overflow: hidden;
  }
  /* Front card (portrait) */
  .card-front {
    left: 110px; top: 150px;
    width: 360px; height: 600px;
  }
  .brand-name {
    font-family: "Exo 2", sans-serif;
    font-weight: 800;
    color: var(--teal-light);
    letter-spacing: 1px;
    text-transform: uppercase;
    display: flex; align-items: center; gap: 10px;
    white-space: nowrap;
  }
  .brand-name .brand-dot {
    width: 14px; height: 14px; background: var(--teal-light); border-radius: 50%; flex: none;
  }
  .card-front .brand-name {
    position: absolute; top: 130px; left: 0; right: 0;
    justify-content: center; font-size: 32px;
  }
  .person {
    position: absolute; top: 255px; left: 0; right: 0; text-align: center;
  }
  .person-name {
    font-weight: 800; font-style: italic; font-size: 27px;
    color: var(--teal-light); letter-spacing: 1px;
  }
  .person-role {
    font-size: 17px; letter-spacing: 1.5px; color: var(--ink); margin-top: 4px;
  }
  .contact {
    position: absolute; top: 340px; left: 0; right: 0;
    text-align: center; font-size: 16px; line-height: 1.45; letter-spacing: .8px;
  }
  .contact .phone-line {
    display: flex; justify-content: center; align-items: center; gap: 8px;
  }
  .contact .phone-line svg { width: 14px; height: 14px; }
  .contact .address { margin-bottom: 12px; }
  .web-band {
    position: absolute; left: 0; right: 0; bottom: 0; height: 58px;
    background: linear-gradient(180deg, var(--teal-light), var(--teal));
    border-top: 4px solid var(--silver);
    display: flex; align-items: center; justify-content: center;
    font-size: 17px; letter-spacing: 1px; color: #0e2a27; font-weight: 600;
  }
  /* Back card (landscape) */
  .card-back {
    left: 520px; top: 300px;
    width: 600px; height: 360px;
  }
  .card-back .brand-name {
    position: absolute; left: 30px; top: 162px; font-size: 24px; gap: 8px;
  }
  .card-back .brand-name .brand-dot { width: 12px; height: 12px; }
  .services {
    position: absolute; left: 318px; top: 70px;
  }
  .services-title {
    font-weight: 800; font-size: 24px; color: var(--teal-light);
    letter-spacing: 1px; margin-bottom: 14px; white-space: nowrap;
  }
  .services-list { list-style: none; }
  .services-list li {
    display: flex; align-items: center; gap: 10px;
    font-size: 15px; letter-spacing: 1px; text-transform: uppercase;
    line-height: 1.95; white-space: nowrap;
  }
  .services-list svg { width: 12px; height: 16px; flex: none; }
</style>
</head>
<body>

<section class="card card-front" aria-label="Business card front">
  <div class="brand-name"><span class="brand-dot"></span>Korvane Works</div>

  <div class="person">
    <div class="person-name">RHETT CALLOWAY</div>
    <div class="person-role">FOUNDER</div>
  </div>

  <div class="contact">
    <p class="address">PO BOX 417 Ridgeline Road<br>2nd street Ballarat</p>
    <p class="phone-line">
      <svg viewBox="0 0 14 14" aria-hidden="true"><circle cx="7" cy="7" r="7" fill="var(--teal-light)"/><rect x="4.5" y="3" width="5" height="8" rx="1" fill="#0b0c0d"/></svg>
      +61 4120 5583
    </p>
    <p class="phone-line">
      <svg viewBox="0 0 14 14" aria-hidden="true"><circle cx="7" cy="7" r="7" fill="var(--teal-light)"/><path d="M4 5.5 Q7 3 10 5.5 L9 7 L5 7 Z M4.5 8 H9.5 V10 H4.5 Z" fill="#0b0c0d"/></svg>
      +61 4120 5583
    </p>
    <p>info@korvaneworks.com</p>
  </div>

  <div class="web-band">www.korvaneworks.com</div>
</section>

<section class="card card-back" aria-label="Business card back">
  <div class="brand-name"><span class="brand-dot"></span>Korvane Works</div>

  <div class="services">
    <h2 class="services-title">SERVICES I OFFER</h2>
    <ul class="services-list">
      <li><svg viewBox="0 0 12 16" aria-hidden="true"><polygon points="7,0 1,9 5,9 4,16 11,6 7,6" fill="var(--teal-light)"/></svg>Breakdowns</li>
      <li><svg viewBox="0 0 12 16" aria-hidden="true"><polygon points="7,0 1,9 5,9 4,16 11,6 7,6" fill="var(--teal-light)"/></svg>Field Service</li>
      <li><svg viewBox="0 0 12 16" aria-hidden="true"><polygon points="7,0 1,9 5,9 4,16 11,6 7,6" fill="var(--teal-light)"/></svg>A/C Systems</li>
      <li><svg viewBox="0 0 12 16" aria-hidden="true"><polygon points="7,0 1,9 5,9 4,16 11,6 7,6" fill="var(--teal-light)"/></svg>Machine Rewires</li>
      <li><svg viewBox="0 0 12 16" aria-hidden="true"><polygon points="7,0 1,9 5,9 4,16 11,6 7,6" fill="var(--teal-light)"/></svg>Mine Site Vehicle Fit Outs</li>
    </ul>
  </div>
</section>

</body>
</html>
```